Affordable, luxury, car transportation company needs a flyer design for advertisement

I need a flyer to advertise my business "PL Harbor Wheels". This is a private car transportation service that aims to be cheaper than all other limousine companies, and more reliable and luxurious than Zipto/taxi.

I am envisioning a stylized design with a fat, unkempt, dirty taxi cab driver on the left (indicating the lack of luxury with taxi service), and a snooty limousine driver, holding piles of cash on the right side (indicating the expensiveness of limo service), and then an image of my business being in between the two, indicating that my company is the perfect compromise of luxury and affordability. The vehicle is a 2023 Varnel Kestra Plus plug-in hybrid electric car, with black leather interior.

I am not "married" to the aforementioned design. But I want the flyer to indicate that my business is the perfect compromise on luxury and affordability. It is more reliable and luxurious than taxi/rideshare but much cheaper than a limousine company.

The flyer should also have the company name, logo, and website address. For inspiration, please visit the website https://www.plharborwheels.example

Industry/Entity Type

Private car transportation. Chauffeur service.

Requirements
Must have
• Company name, logo, website address. Indicate that we offer the perfect compromise of luxury and affordability

```html
<!DOCTYPE html>
<html lang="en">
<head>
<meta charset="utf-8">
<title>PL Harbor Wheels – Private Car Service Flyer</title>
<link rel="stylesheet" href="https://fonts.googleapis.com/css2?family=Poppins:ital,wght@0,300;0,400;0,600;0,700;0,800;1,700&family=Source+Sans+3:wght@400&display=swap">
<style>
  :root{
    --ink:#0b0b0b;
    --orange:#f7a01b;
    --white:#ffffff;
    --grey-text:#4a4a4a;
    --stage:#8e939b;
    --card-top:#ececec;
    --card-bottom:#f9f9f9;
  }
  *{margin:0;padding:0;box-sizing:border-box}
  html,body{width:1200px;height:1200px;overflow:hidden;background:var(--stage)}
  .stage{position:relative;width:1200px;height:1200px}
  .flyer{
    position:absolute;left:158px;top:31px;width:1263px;height:1624px;
    transform:scale(0.7);transform-origin:top left;
    background:var(--white);overflow:hidden;
    font-family:"Poppins",sans-serif;color:var(--ink);
    box-shadow:0 30px 40px rgba(0,0,0,.35);
  }
  .flyer > *{position:absolute}
  .backdrop{left:0;top:0}
  .brand-name{left:78px;top:160px;padding:4px 10px;color:var(--white);font-weight:600;font-size:27px;letter-spacing:5px;text-transform:uppercase}
  .brand-square{left:78px;top:120px;width:28px;height:28px;background:var(--white)}
  .headline{left:74px;top:225px;line-height:90px;font-size:84px}
  .headline .l1{display:block;color:var(--white);font-weight:400}
  .headline .l2{display:block;color:var(--orange);font-weight:700}
  .headline .l3{display:block;color:var(--white);font-weight:700}
  .tagline{left:78px;top:656px;font-family:"Source Sans 3",sans-serif;color:var(--grey-text);font-size:30px;line-height:36px}
  .tagline p + p{margin-top:18px}
  .book-tag{left:52px;top:846px;width:200px;height:84px;background:var(--ink);color:var(--white);font-size:28px;line-height:84px;padding-left:35px;clip-path:polygon(14% 0,100% 0,100% 100%,14% 100%,0 50%)}
  .big-three{left:226px;top:780px;font-size:200px;font-weight:800;color:var(--orange);line-height:1;text-shadow:0 8px 10px rgba(0,0,0,.25)}
  .easy{left:350px;top:825px;font-size:60px;font-weight:300;line-height:1}
  .steps-word{left:350px;top:888px;font-size:46px;font-weight:700;line-height:1}
  .step-card{left:72px;width:426px;border-radius:20px;background:linear-gradient(180deg,var(--card-top),var(--card-bottom));padding:28px 16px 0 68px}
  .step-card h3{font-size:28px;font-weight:700;display:flex;align-items:center;gap:12px;margin-bottom:10px}
  .step-card .num{width:32px;height:32px;border-radius:50%;background:var(--orange);font-size:22px;display:inline-flex;align-items:center;justify-content:center}
  .step-card p{font-size:16px;line-height:22px;color:var(--grey-text)}
  .step-card p + p{margin-top:10px}
  .step-one{top:1010px;height:173px}
  .step-two{top:1187px;height:168px}
  .step-three{top:1360px;height:195px}
  .step-icon{left:58px;width:64px;height:64px;border:2px solid var(--ink);border-radius:6px;background:var(--white);display:flex;align-items:center;justify-content:center}
  .services-heading{left:561px;top:1045px;width:640px;font-size:25px;font-weight:700;font-style:italic;line-height:32px}
  .rule-dark{left:561px;top:1154px;width:36px;height:6px;background:var(--ink)}
  .rule-orange{left:600px;top:1156px;width:663px;height:2px;background:var(--orange)}
  .about{left:561px;top:1172px;width:660px;font-size:16px;line-height:22px;color:var(--grey-text)}
  .coverage{left:561px;top:1259px;width:654px;height:232px;border-radius:18px;background:linear-gradient(180deg,#1a1a1a,#000);border:3px solid var(--ink);overflow:hidden}
  .coverage h4{height:42px;margin:2px;border-radius:14px 14px 14px 14px;background:var(--orange);font-size:28px;font-weight:700;line-height:42px;padding-left:16px}
  .coverage ul{list-style:none;position:absolute;top:62px;color:var(--white);font-size:19px;line-height:22px}
  .coverage li{position:relative;padding-left:26px;margin-bottom:11px}
  .coverage li::before{content:"";position:absolute;left:0;top:4px;width:16px;height:16px;border-radius:50%;background:var(--orange)}
  .coverage li::after{content:"";position:absolute;left:5px;top:7px;width:4px;height:7px;border:solid var(--ink);border-width:0 2px 2px 0;transform:rotate(40deg)}
  .coverage .col-a{left:18px;width:340px}
  .coverage .col-b{left:372px;width:270px}
  .cta{left:540px;top:1512px;width:390px;height:36px;background:var(--orange);clip-path:polygon(8% 0,100% 0,94% 100%,0 100%);font-weight:700;font-size:24px;line-height:38px;text-align:center;padding-left:10px}
  .web{left:922px;top:1512px;width:341px;height:34px;background:var(--white);clip-path:polygon(8% 0,100% 0,100% 100%,0 100%);font-size:18px;line-height:34px;padding-left:42px}
  .email{left:617px;top:1556px;color:var(--white);font-size:21px}
  .email b{font-weight:600}
</style>
</head>
<body>
<div class="stage">
  <div class="flyer">
    <svg class="backdrop" width="1263" height="1624" viewBox="0 0 1263 1624">
      <defs>
        <linearGradient id="photoTone" x1="0" y1="0" x2="1" y2="0">
          <stop offset="0" stop-color="#000" stop-opacity="1"/>
          <stop offset="0.2" stop-color="#4a4430" stop-opacity="0.7"/>
          <stop offset="0.55" stop-color="#b18f3a"/>
          <stop offset="1" stop-color="#d8aa2c"/>
        </linearGradient>
        <linearGradient id="carTone" x1="0" y1="0" x2="0" y2="1">
          <stop offset="0" stop-color="#c8d2dc" stop-opacity="0"/>
          <stop offset="0.4" stop-color="#b9c3cc"/>
          <stop offset="1" stop-color="#e9ecef"/>
        </linearGradient>
        <clipPath id="darkArea">
          <polygon points="0,0 1263,0 1263,1030 1010,1030 440,588 375,632 252,512 125,617 95,590 0,650"/>
        </clipPath>
      </defs>
      <polygon points="0,0 1263,0 1263,1030 1010,1030 440,588 375,632 252,512 125,617 95,590 0,650" fill="#000"/>
      <rect role="img" aria-label="Photo of a scruffy taxi driver in a mustard shirt standing in front of yellow cabs" x="480" y="0" width="783" height="1030" fill="url(#photoTone)" clip-path="url(#darkArea)"/>
      <polyline points="0,642 95,580 125,606 252,500 375,620 440,575 1020,1030" fill="none" stroke="#6a6a6a" stroke-width="6"/>
      <line x1="10" y1="600" x2="60" y2="565" stroke="var(--orange)" stroke-width="14" stroke-linecap="round"/>
      <line x1="620" y1="670" x2="720" y2="745" stroke="var(--orange)" stroke-width="16" stroke-linecap="round"/>
      <line x1="740" y1="725" x2="790" y2="765" stroke="var(--orange)" stroke-width="10" stroke-linecap="round"/>
      <polygon points="880,930 1263,950 1263,1030 1000,1030" fill="#000"/>
      <polyline points="860,900 960,960 1263,960" fill="none" stroke="var(--orange)" stroke-width="8"/>
      <polyline points="880,880 990,945 1263,945" fill="none" stroke="var(--orange)" stroke-width="4"/>
      <rect role="img" aria-label="Photo of the white Varnel Kestra Plus SUV with mountains behind" x="500" y="760" width="420" height="255" rx="30" fill="url(#carTone)"/>
      <rect x="0" y="1597" width="210" height="27" fill="var(--orange)"/>
      <polygon points="200,1624 500,1548 540,1512 1263,1508 1263,1624" fill="#000"/>
      <polygon points="190,1624 500,1534 540,1500 1263,1500 1263,1508 540,1510 505,1546 215,1624" fill="#fff"/>
    </svg>

    <div class="brand-square"></div>
    <div class="brand-name">PL Harbor Wheels</div>

    <h1 class="headline">
      <span class="l1">PL Harbor</span>
      <span class="l2">Wheels Private</span>
      <span class="l3">Car Service</span>
    </h1>

    <div class="tagline">
      <p>Colorado Springs Based | Serving<br>Southern Colorado and Beyond</p>
      <p>Affordable Luxury Transportation</p>
    </div>

    <div class="book-tag">Book With</div>
    <div class="big-three">3</div>
    <div class="easy">Easy</div>
    <div class="steps-word">Steps</div>

    <section class="step-card step-one">
      <h3><span class="num">1</span>Check Price</h3>
      <p>Colorado Springs Based | Serving<br>Southern Colorado and Beyond</p>
      <p>Affordable Luxury Transportation</p>
    </section>
    <div class="step-icon" style="top:1065px">
      <svg width="40" height="40" viewBox="0 0 40 40" fill="none" stroke="#000" stroke-width="3"><circle cx="30" cy="9" r="5"/><path d="M30 14v4H14a6 6 0 0 0 0 12h18"/><circle cx="9" cy="30" r="4" fill="#000"/></svg>
    </div>

    <section class="step-card step-two">
      <h3><span class="num">2</span>Submit a Request</h3>
      <p>with our intuitive form. Enter your pickup/ dropoff addresses, questions, details, and special requests. No payment due yet.</p>
    </section>
    <div class="step-icon" style="top:1240px">
      <svg width="44" height="36" viewBox="0 0 44 36"><path d="M6 18l5-10h20l6 10h3v10H4V18z" fill="#000"/><rect x="14" y="11" width="7" height="6" fill="#fff"/><rect x="23" y="11" width="8" height="6" fill="#fff"/><circle cx="12" cy="28" r="4" fill="#fff" stroke="#000" stroke-width="3"/><circle cx="32" cy="28" r="4" fill="#fff" stroke="#000" stroke-width="3"/></svg>
    </div>

    <section class="step-card step-three">
      <h3><span class="num">3</span>Payment</h3>
      <p>A human will review your request for price and availability accuracy, then you will receive an email with a link to a secure payment processing page. You will receive your driver's private phone number.</p>
    </section>
    <div class="step-icon" style="top:1424px">
      <svg width="30" height="44" viewBox="0 0 30 44"><rect x="3" y="2" width="24" height="40" rx="4" fill="none" stroke="#000" stroke-width="4"/><circle cx="15" cy="35" r="2.5" fill="#000"/></svg>
    </div>

    <h2 class="services-heading">Private Car Transportation. Airport Shuttles, Ski Resort Transfers, and Southern Colorado Intercity Transportation.</h2>
    <div class="rule-dark"></div>
    <div class="rule-orange"></div>
    <p class="about">PL Harbor Wheels offers private, affordable, luxury car services in Southern Colorado and throughout the state. Denver International Airport (DEN), Colorado Springs Airport (COS), and more.</p>

    <div class="coverage">
      <h4>Connecting Southern Colorado</h4>
      <ul class="col-a">
        <li>Colorado Springs Airport (COS)</li>
        <li>Denver International Airport (DEN) a.k.a DIA</li>
        <li>Colorado Springs</li>
        <li>Woodland Park and Teller County</li>
      </ul>
      <ul class="col-b">
        <li>Pueblo, La Junta, Trinidad, Durango</li>
        <li>Ski Resorts: Breckenridge, Vail, Aspen, Telluride</li>
        <li>And More!</li>
      </ul>
    </div>

    <div class="cta">BOOK YOUR RIDE TODAY!</div>
    <div class="web">www.plharborwheels.example</div>
    <p class="email"><b>General inquiries email:</b>&nbsp; info@plharborwheels.example</p>
  </div>
</div>
</body>
</html>
```